Nutrient Guild of Meridia Website Creation

Nutrient Guild of Meridia seeks a membership website that is visually dynamic, suitable for all who seek knowledge and inspiration about maximizing their health and wellbeing. see nutrientguildofmeridia.com

Target Market(s)

Scientists, Media, Medical Professionals, Nutritionists, Public

Industry/Entity Type

Nutrition

Number of Pages Required

5+ page

Font styles to use
Sans Serif

Colors
0355a3
ec1f27

Requirements
Must have
• Large Pictures, full screen
• Areas for video, blog, articles
• Membership sign in/ Public Access
• Easy to Edit/Add Content
• Merchant Ready
• please check out http://greenleafcircle.org This is what I want it to resemble.
Nice to have
• Red White and Blue but not static, old fashioned, but upbeat.
• Movement - subtle
Should not have
• Should not look Governmental-ish
• Flat look
• Small page
• should not look like the basic site at www.nutrientguildofmeridia.com

```html
<!DOCTYPE html>
<html lang="en">
<head>
<meta charset="utf-8">
<title>Nutrient Guild of Meridia</title>
<link rel="stylesheet" href="https://fonts.googleapis.com/css2?family=Lato:ital,wght@0,300;0,400;0,700;0,900;1,900&display=swap">
<style>
  :root{
    --navy:#0b0c4f;
    --red:#c1121f;
    --red-bright:#e3232b;
    --text:#4a4a4a;
    --heading:#1c1c3a;
    --panel:#f2f2f2;
    --green-dark:#3e9b1e;
    --green:#62c02d;
    --rule:#9aa0b4;
  }
  *{box-sizing:border-box;margin:0;padding:0}
  html,body{width:1200px;height:1200px;overflow:hidden;background:#fff;font-family:'Lato',sans-serif;color:var(--text)}
  .stage{position:absolute;left:0;top:0;width:1500px;height:1500px;transform:scale(.8);transform-origin:0 0}
  .page{position:absolute;left:456px;top:0;width:581px;height:1500px;background:#fff}
  .abs{position:absolute}

  /* header */
  .brand{left:30px;top:7px;display:flex;align-items:center;gap:5px}
  .brand-dot{width:52px;height:52px;border-radius:50%;background:var(--navy)}
  .brand-name{font-size:8px;font-weight:700;color:var(--navy);width:70px;line-height:1.2}
  .social{top:6px;width:18px;height:18px;border-radius:50%;border:1.5px solid var(--navy)}
  .login{left:479px;top:6px;width:78px;height:18px;border:1px solid var(--red);color:var(--red);font-size:7.5px;display:flex;align-items:center;justify-content:center;letter-spacing:.2px}
  .nav{top:32px;left:208px;display:flex;gap:13px;font-size:8px;color:#333;text-transform:uppercase;white-space:nowrap}
  .nav .active{color:var(--red)}

  /* hero */
  .hero{left:0;top:48px;width:581px;height:230px;background:radial-gradient(circle at 40% 50%,var(--green) 0%,var(--green-dark) 100%);overflow:hidden}
  .hero-photo{position:absolute;left:234px;top:0;width:347px;height:230px;background:linear-gradient(135deg,#e9b79a 0%,#e2425d 45%,#d9dde3 75%,#c89a7c 100%)}
  .hero-title{position:absolute;left:50px;top:80px;font-size:25px;font-weight:900;font-style:italic;color:#fff;line-height:30px;text-transform:uppercase}
  .hero-arrow{position:absolute;top:100px}

  /* section headings */
  .sec-title{left:0;width:581px;text-align:center;font-size:18px;font-weight:400;color:var(--heading);text-transform:uppercase}
  .sec-rule{left:0;width:581px}
  .btn{border:1px solid var(--red);color:var(--red);font-size:9.5px;display:flex;align-items:center;justify-content:center;gap:3px;background:#fff}

  .about-text{left:27px;top:340px;width:400px;font-size:7.8px;line-height:14.5px;font-weight:300;color:#333}
  .portrait{left:445px;top:335px;width:107px;height:107px;background:linear-gradient(180deg,#d8dde2 0%,#a89384 45%,#3b2b2b 100%);border:1px solid #ddd}
  .caption{left:430px;top:446px;width:137px;text-align:center;font-size:7.5px;line-height:11px;color:var(--navy)}

  .panel{left:0;width:581px;background:var(--panel)}
  .cert{left:34px;top:565px;width:147px;height:126px;border:4px solid #333;background:#fff;padding:8px;box-shadow:0 1px 3px rgba(0,0,0,.4)}
  .cert-inner{width:100%;height:100%;background:linear-gradient(135deg,#eef1f8,#c7cfe2)}
  .member-text{left:208px;top:564px;width:350px;font-size:7.8px;line-height:13.7px;font-weight:300;color:#333}

  .video-sub{left:0;top:796px;width:581px;text-align:center;font-size:7.5px;line-height:14px;color:#333}
  .video-main{left:25px;top:833px;width:353px;height:232px;border:1px solid #ccc;padding:3px;background:#fff}
  .video-screen{position:relative;width:100%;height:100%;background:linear-gradient(160deg,#5d5955 0%,#2d2a28 60%,#1a1817 100%);overflow:hidden}
  .video-label{position:absolute;left:2px;top:9px;font-size:12px;color:#fff;white-space:nowrap}
  .video-thumb{left:392px;width:164px;height:75px;border:1px solid #333;background:linear-gradient(160deg,#5d5955,#1f1d1c);overflow:hidden}
  .thumb-label{position:absolute;left:3px;top:2px;font-size:4.5px;color:#fff;white-space:nowrap}

  .blog-img{top:1155px;width:168px;height:108px;border:1px solid #7c8096}
  .date{width:19px;height:33px;top:1263px;font-size:7.5px;color:#fff;text-align:center}
  .date .d{background:var(--navy);height:16px;line-height:16px}
  .date .m{background:var(--red);height:17px;line-height:17px}
  .blog-text{top:1269px;width:140px;font-size:7px;line-height:11.4px;font-weight:300;color:#333}
  .blog-btn{top:1344px;width:56px;height:15px;font-size:7.5px}

  .cta{left:0;top:1394px;width:581px;height:82px;background:var(--navy);color:#fff;text-align:center;font-size:18px;line-height:23px;padding-top:18px}
  .cta .phone{color:var(--red-bright)}
  .foot{top:1485px;font-size:6.5px;color:#555}
</style>
</head>
<body>
<div class="stage">
<div class="page">

  <header>
    <div class="abs brand"><span class="brand-dot"></span><span class="brand-name">Nutrient Guild of Meridia</span></div>
    <span class="abs social" style="left:397px"></span>
    <span class="abs social" style="left:423px"></span>
    <span class="abs social" style="left:449px"></span>
    <a class="abs login">MEMBER LOGIN &rarr;</a>
    <nav class="abs nav"><span class="active">Home</span><span>About Us</span><span>Membership Opportunitie</span><span>Video Library</span><span>Contact Us</span></nav>
  </header>

  <section class="abs hero">
    <div class="hero-photo" role="img" aria-label="Smiling family of three, a girl riding on her father's shoulders"></div>
    <h1 class="hero-title">Food for<br>Micronutrient<br>Thought</h1>
    <svg class="hero-arrow" style="left:9px" width="10" height="26"><path d="M8 1 L2 13 L8 25" stroke="#fff" stroke-width="1.3" fill="none"/></svg>
    <svg class="hero-arrow" style="left:563px" width="10" height="26"><path d="M2 1 L8 13 L2 25" stroke="#fff" stroke-width="1.3" fill="none"/></svg>
  </section>

  <!-- About -->
  <h2 class="abs sec-title" style="top:301px">About Us</h2>
  <svg class="abs sec-rule" style="top:321px" width="581" height="10"><line x1="240" y1="4.5" x2="341" y2="4.5" stroke="var(--rule)" stroke-width="1"/><circle cx="290.5" cy="4.5" r="2.8" fill="#fff" stroke="var(--rule)"/></svg>
  <p class="abs about-text">NGM – the Nutrient Guild of Meridia's new official website reflects the core mission – to keep it's members and the Nation up-to-date with all aspects of vitamin and mineral health. NGM promotes the study of vitamins and minerals, furthers the exchange of research and professional experience between members, and provides scientific articles, topical information, web resources, and referrals for health care specialists in the field. NGM also organizes and participates in national and international events related to the topic. We welcome all interested in the field to join our society.</p>
  <a class="abs btn" style="left:25px;top:444px;width:70px;height:20px">Read More &rarr;</a>
  <div class="abs portrait" role="img" aria-label="Portrait of the guild founder in a suit"></div>
  <p class="abs caption">Elias M. Varden, MD,<br>MPH &nbsp;NGM Founder &amp; CEO</p>

  <!-- Membership -->
  <div class="abs panel" style="top:493px;height:240px"></div>
  <h2 class="abs sec-title" style="top:519px">Membership Opportunities</h2>
  <svg class="abs sec-rule" style="top:540px" width="581" height="10"><line x1="163" y1="4.5" x2="418" y2="4.5" stroke="var(--rule)"/><circle cx="290.5" cy="4.5" r="2.8" fill="var(--panel)" stroke="var(--rule)"/></svg>
  <div class="abs cert"><div class="cert-inner" role="img" aria-label="Framed guild member certificate"></div></div>
  <div class="abs member-text">
    <p>Join The Nutrient Guild of Meridia Today – Find Your Membership Level – Please supply verifiable documentation for special categories.</p>
    <p style="margin-top:2px">Members will receive a beautiful Nutrient Guild Member Certificate (or we can send it 11X14 matted and framed $50), access to monthly NGM Newsletter, discounted access to Conferences, Educational Materials, Special products, and merchandise offers. &nbsp;Full Members will be asked to participate in important votes and Society business dealings. &nbsp;We invite you to join us today, and thank you!</p>
  </div>
  <a class="abs btn" style="left:208px;top:671px;width:94px;height:20px">View Our Pricing &rarr;</a>

  <!-- Video -->
  <h2 class="abs sec-title" style="top:759px">Video Library</h2>
  <svg class="abs sec-rule" style="top:780px" width="581" height="10"><line x1="222" y1="4.5" x2="359" y2="4.5" stroke="var(--rule)"/><circle cx="290.5" cy="4.5" r="2.8" fill="#fff" stroke="var(--rule)"/></svg>
  <p class="abs video-sub">Dr. Elias M. Varden, MD, MPH presented the MOST 2010 Paper at the 10th International Conference,<br>Nutrition &amp; Diagnostics September 4 -7, 2010 in Prague, Czech Republic.</p>
  <div class="abs video-main">
    <div class="video-screen" role="img" aria-label="Conference lecture video: speaker at a podium before a projected slide">
      <span class="video-label">Varden - 2010 Nutrition Conference in Prague...</span>
      <svg style="position:absolute;left:135px;top:94px" width="48" height="34"><rect width="48" height="34" rx="8" fill="var(--red)"/><path d="M19 10 L31 17 L19 24Z" fill="#fff"/></svg>
    </div>
  </div>
  <div class="abs video-thumb" style="top:833px" role="img" aria-label="Conference video thumbnail"><span class="thumb-label">Dr. Varden - 2010 Nutrition Conference in Prague</span><svg style="position:absolute;left:75px;top:33px" width="14" height="10"><rect width="14" height="10" rx="3" fill="#222"/><path d="M5 2.5 L9.5 5 L5 7.5Z" fill="#fff"/></svg></div>
  <div class="abs video-thumb" style="top:912px" role="img" aria-label="Conference video thumbnail"><span class="thumb-label">Dr. Varden - 2010 Nutrition Conference in Prague</span><svg style="position:absolute;left:75px;top:33px" width="14" height="10"><rect width="14" height="10" rx="3" fill="#222"/><path d="M5 2.5 L9.5 5 L5 7.5Z" fill="#fff"/></svg></div>
  <div class="abs video-thumb" style="top:990px" role="img" aria-label="Conference video thumbnail"><span class="thumb-label">Dr. Varden - 2010 Nutrition Conference in Prague</span><svg style="position:absolute;left:75px;top:33px" width="14" height="10"><rect width="14" height="10" rx="3" fill="#222"/><path d="M5 2.5 L9.5 5 L5 7.5Z" fill="#fff"/></svg></div>

  <!-- Blog -->
  <div class="abs panel" style="top:1094px;height:300px"></div>
  <h2 class="abs sec-title" style="top:1112px">Read Our Blog</h2>
  <svg class="abs sec-rule" style="top:1133px" width="581" height="10"><line x1="219" y1="4.5" x2="362" y2="4.5" stroke="var(--rule)"/><circle cx="290.5" cy="4.5" r="2.8" fill="var(--panel)" stroke="var(--rule)"/></svg>

  <div class="abs blog-img" style="left:25px;background:linear-gradient(135deg,#f4f4f4,#d9a88c 55%,#efefef)" role="img" aria-label="Happy family with two children"></div>
  <div class="abs date" style="left:25px"><div class="d">30</div><div class="m">OCT</div></div>
  <p class="abs blog-text" style="left:54px">Lorem ipsum dolor sit amet, consectetur adipiscing elit. Morbi ullamcorper purus vel mauris faucibus, et pulvinar sapien pretium. Pellentesque placerat sapien a orci semper, vitae iaculis neque blandit. Vestibulum ante...</p>
  <a class="abs btn blog-btn" style="left:54px">Read More &rarr;</a>

  <div class="abs blog-img" style="left:207px;background:linear-gradient(180deg,#f7f7f7,#e6c2ae 60%,#f2f2f2)" role="img" aria-label="Woman taking a vitamin capsule"></div>
  <div class="abs date" style="left:207px"><div class="d">30</div><div class="m">OCT</div></div>
  <p class="abs blog-text" style="left:237px">Lorem ipsum dolor sit amet, consectetur adipiscing elit. Morbi ullamcorper purus vel mauris faucibus, et pulvinar sapien pretium. Pellentesque placerat sapien a orci semper, vitae iaculis neque blandit. Vestibulum ante...</p>
  <a class="abs btn blog-btn" style="left:237px">Read More &rarr;</a>

  <div class="abs blog-img" style="left:389px;background:radial-gradient(circle at 50% 50%,#e8453a 0%,#f2a48c 35%,#fff 65%)" role="img" aria-label="Cut apple with vitamin letter spheres"></div>
  <div class="abs date" style="left:389px"><div class="d">30</div><div class="m">OCT</div></div>
  <p class="abs blog-text" style="left:419px">Lorem ipsum dolor sit amet, consectetur adipiscing elit. Morbi ullamcorper purus vel mauris faucibus, et pulvinar sapien pretium. Pellentesque placerat sapien a orci semper, vitae iaculis neque blandit. Vestibulum ante...</p>
  <a class="abs btn blog-btn" style="left:419px">Read More &rarr;</a>

  <!-- CTA + footer -->
  <div class="abs cta">For Any Information, Feel Free To<br>Call us at: <span class="phone">(555)-014-2231</span></div>
  <p class="abs foot" style="left:27px">Home &nbsp;|&nbsp; About Us &nbsp;|&nbsp; Contact Us &nbsp;|&nbsp; Membership &nbsp;|&nbsp; Opportunities &nbsp;|&nbsp; Video Library</p>
  <p class="abs foot" style="left:385px">© 2015 Nutrient Guild of Meridia. All right reserved</p>

</div>
</div>
</body>
</html>
```